Vacation giveaway landing page design

We are giving away a holiday/vacation to Rome and we need a landing page designed that will entice people to enter their email address for a chance to win!

Full brief, examples and everything else can be found in this document: https://files.brintowle.net/papers/p/4-wxkoppTR7mnbQ2vyLazcR5xsjfPe3lhmwcKt27r/view?mode=linked

1 page

```html
<!DOCTYPE html>
<html lang="en">
<head>
<meta charset="utf-8">
<title>Wishcatcher — Win a Holiday to Rome</title>
<link rel="stylesheet" href="https://fonts.googleapis.com/css2?family=Cabin:wght@500;600;700&family=Roboto:wght@400;500;700;900&display=swap">
<style>
:root{
  --red:#f04a45;
  --teal:#2a9a92;
  --teal-dark:#23857e;
  --ink:#222;
  --muted:#6b6b6b;
  --line:#e6e6e6;
  --white:#fff;
}
*{box-sizing:border-box;margin:0;padding:0}
html,body{width:1200px;height:2177px;overflow:hidden;background:var(--white);font-family:Roboto,sans-serif;color:var(--ink)}
.page{position:relative;width:1200px;height:2177px;overflow:hidden}
.abs{position:absolute}

/* hero */
.hero-photo{position:absolute;left:0;top:0;width:1200px;height:1020px;
  background:
   radial-gradient(ellipse 420px 260px at 300px 720px,#3fc1b0 0%,rgba(63,193,176,0) 70%),
   radial-gradient(ellipse 380px 220px at 1050px 420px,#2a8fb8 0%,rgba(42,143,184,0) 70%),
   radial-gradient(ellipse 500px 300px at 500px 250px,#6d8a45 0%,rgba(109,138,69,0) 75%),
   linear-gradient(180deg,#3b6fa8 0%,#4f7d52 22%,#5a8a3c 45%,#3aa596 70%,#7a7a4a 100%)}
.hero-shade{position:absolute;left:0;top:0;width:1200px;height:1020px;background:linear-gradient(90deg,rgba(0,0,0,.18),rgba(0,0,0,0) 45%,rgba(0,0,0,.22))}
.wave{position:absolute;left:0;top:760px}

.brand{position:absolute;display:flex;align-items:center;gap:10px;font-family:Cabin,sans-serif;font-weight:700;letter-spacing:1px}
.brand-dot{border-radius:50%;border:3px solid currentColor}
.brand--header{left:112px;top:60px;color:var(--white);font-size:30px}
.brand--header .brand-dot{width:62px;height:62px}
.brand--band{left:123px;top:918px;color:var(--teal);font-size:44px}
.brand--band .brand-dot{width:74px;height:74px}
.brand--footer{left:112px;top:1922px;color:var(--white);font-size:36px}
.brand--footer .brand-dot{width:70px;height:70px}

.menu{position:absolute;left:1046px;top:57px;width:43px}
.menu span{display:block;height:6px;background:var(--white);border-radius:2px;margin-bottom:8px}

.hero-pre{left:112px;top:300px;font-family:Cabin,sans-serif;font-weight:600;font-size:32px;color:var(--white);letter-spacing:1px}
.hero-title{left:110px;top:346px;font-weight:700;font-size:59px;color:var(--white);letter-spacing:-1px}
.perks{left:112px;top:452px;list-style:none;font-family:Cabin,sans-serif;font-weight:600;font-size:24px;color:var(--white)}
.perks li{display:flex;align-items:center;gap:20px;height:48px}

.offer{left:769px;top:256px;color:var(--white);width:330px}
.offer h3{font-family:Cabin,sans-serif;font-weight:700;font-size:25px;margin-bottom:26px}
.plan{display:flex;align-items:center;gap:18px;font-family:Cabin,sans-serif;font-weight:600;font-size:20px;margin-bottom:14px}
.box{width:15px;height:15px;border:2px solid var(--white);border-radius:3px;flex:none}
.plan-list{list-style:none;padding-left:34px;font-weight:500;font-size:15px;margin-bottom:20px}
.plan-list li{height:27px;display:flex;align-items:center;gap:12px}

.entry{left:769px;top:637px;width:322px;color:var(--white)}
.entry h3{font-family:Cabin,sans-serif;font-weight:700;font-size:25px;margin-bottom:14px}
.email{height:43px;background:var(--white);color:#888;font-size:14px;padding:0 14px;display:flex;align-items:center}
.consent{display:flex;gap:10px;margin-top:16px;font-size:14px;line-height:23px;text-align:justify}
.consent .box{margin-top:5px;width:13px;height:13px}
.submit{position:absolute;left:202px;top:189px;width:119px;height:43px;background:var(--red);color:var(--white);font-weight:700;font-size:18px;display:flex;align-items:center;justify-content:center}

/* winners */
.section-ghost{left:0;top:1078px;width:1200px;text-align:center;font-weight:900;font-size:86px;color:#f1f1f1;letter-spacing:1px}
.section-title{left:0;top:1120px;width:1200px;text-align:center;font-weight:700;font-size:43px;color:var(--ink);letter-spacing:-.5px}
.card{position:absolute;top:1216px;width:294px;height:497px;background:var(--white);box-shadow:0 0 6px rgba(0,0,0,.12);text-align:center}
.card-photo{position:absolute;left:4px;top:4px;width:286px;height:186px}
.photo-a{background:linear-gradient(135deg,#b8a79a,#6c5a52 60%,#3a3232)}
.photo-b{background:linear-gradient(135deg,#8d8172,#c9b9a2 50%,#6f6659)}
.photo-c{background:linear-gradient(135deg,#9b8e82,#4c4d52 55%,#2c2a2c)}
.card-curve{position:absolute;left:0;top:180px}
.card-title{position:absolute;left:0;top:234px;width:100%;font-weight:500;font-size:21px;line-height:28px;color:var(--ink)}
.card-text{position:absolute;left:18px;top:290px;width:258px;font-size:16px;line-height:29px;color:var(--muted)}
.card-btn{position:absolute;left:75px;top:405px;width:145px;height:43px;border:1px solid #ddd;color:var(--teal);font-weight:500;font-size:15px;display:flex;align-items:center;justify-content:center;gap:4px}
.card-btn--solid{background:var(--teal);border-color:var(--teal);color:var(--white)}
.card-stats{position:absolute;left:24px;right:24px;top:476px;display:flex;align-items:center;font-size:15px;color:var(--muted)}
.card-stats .sep{margin:0 12px}
.card-stats .share{margin-left:auto}
.card-stats svg{vertical-align:-2px;margin-right:3px}

/* footer */
.footer{position:absolute;left:0;top:1827px;width:1200px;height:350px;background:var(--teal)}
.footer-col{position:absolute;color:var(--white)}
.footer-col h4{font-weight:500;font-size:23px;margin-bottom:24px}
.contact{left:550px;top:80px;font-size:16px}
.contact p{display:flex;align-items:center;gap:22px;height:37px}
.follow{left:922px;top:80px}
.socials{display:flex;gap:11px;margin-top:-2px}
.social{width:47px;height:47px;border:2px solid var(--white);border-radius:50%;display:flex;align-items:center;justify-content:center}
.footer-rule{position:absolute;left:112px;top:264px;width:976px;height:1px;background:rgba(255,255,255,.6)}
.copyright{position:absolute;left:0;top:296px;width:1200px;text-align:center;color:var(--white);font-size:17px}
.live{position:absolute;left:112px;top:316px;width:157px;height:34px;background:var(--red);color:var(--white);font-weight:500;font-size:17px;display:flex;align-items:center;justify-content:center;gap:8px}
</style>
</head>
<body>
<div class="page">

  <div class="hero-photo" role="img" aria-label="Aerial photo of a green rocky coastline with a turquoise bay and beach"></div>
  <div class="hero-shade"></div>

  <svg class="wave" width="1200" height="260" viewBox="0 760 1200 260" aria-hidden="true">
    <path d="M0 883 C90 800 170 770 250 784 C420 810 650 980 943 1015 C1060 1025 1150 960 1200 900 L1200 1020 L0 1020 Z" fill="var(--red)"/>
    <path d="M0 943 C90 860 170 828 250 832 C430 845 660 985 943 1010 C1060 1018 1150 965 1200 905 L1200 1020 L0 1020 Z" fill="var(--white)"/>
    <path d="M960 1016 C1070 1016 1150 965 1200 905 L1200 1020 Z" fill="var(--white)"/>
  </svg>

  <div class="brand brand--header"><span class="brand-dot"></span>WISHCATCHER</div>
  <div class="menu" aria-label="Menu"><span></span><span></span><span></span></div>

  <div class="abs hero-pre">We Are The</div>
  <h1 class="abs hero-title">WISHCATCHERS</h1>
  <ul class="abs perks">
    <li><svg width="26" height="22" viewBox="0 0 26 22" fill="none" stroke="#fff" stroke-width="2"><path d="M2 9h5v11H2zM7 10l5-8c2 0 3 1 2 4l-1 3h10a2 2 0 010 4h-2a2 2 0 010 4h-2a2 2 0 01-1 3H7"/></svg>Monthly Entry Into A Prize Draw</li>
    <li><svg width="26" height="22" viewBox="0 0 26 22" fill="none" stroke="#fff" stroke-width="2"><path d="M2 9h5v11H2zM7 10l5-8c2 0 3 1 2 4l-1 3h10a2 2 0 010 4h-2a2 2 0 010 4h-2a2 2 0 01-1 3H7"/></svg>Weekly Discount Emails</li>
    <li><svg width="26" height="22" viewBox="0 0 26 22" fill="none" stroke="#fff" stroke-width="2"><path d="M2 9h5v11H2zM7 10l5-8c2 0 3 1 2 4l-1 3h10a2 2 0 010 4h-2a2 2 0 010 4h-2a2 2 0 01-1 3H7"/></svg>Monthly Digital Magazine</li>
  </ul>

  <div class="abs offer">
    <h3>What We Want Now:</h3>
    <div class="plan"><span class="box"></span>5 Entries &amp; weekly deals</div>
    <ul class="plan-list">
      <li>»&nbsp; Weekly Deals Email (?)</li>
      <li>»&nbsp; Save £100's on Holidays (?)</li>
      <li>»&nbsp; Monthly Magazine (?)</li>
      <li>»&nbsp; 15 Entries Every Month</li>
    </ul>
    <div class="plan"><span class="box"></span>1 Entry</div>
    <ul class="plan-list">
      <li>»&nbsp; Save £100's on Holidays (?)</li>
      <li>»&nbsp; Monthly Magazine (?)</li>
      <li>»&nbsp; 1 Entries Every Month</li>
    </ul>
  </div>

  <div class="abs entry">
    <h3>Free Entry:</h3>
    <div class="email">Email Address</div>
    <div class="consent"><span class="box"></span><span>We want a completely new landing page which only features free entry into a prize draw via inputting your email address.</span></div>
    <div class="submit">SUBMIT</div>
  </div>

  <div class="brand brand--band"><span class="brand-dot"></span>WISHCATCHER</div>

  <div class="abs section-ghost" aria-hidden="true">OUR WINNERS</div>
  <h2 class="abs section-title">PREVIOUS WINNERS</h2>

  <article class="card" style="left:112px">
    <div class="card-photo photo-a" role="img" aria-label="Photo of two smiling winners holding wine glasses"></div>
    <svg class="card-curve" width="294" height="20" viewBox="0 0 294 20"><path d="M14 6 Q147 30 280 6 Q147 18 14 6Z" fill="var(--red)"/></svg>
    <h3 class="card-title">THIS MONTH WINNER<br>PRIZE</h3>
    <p class="card-text">Lorem ipsum dolor sit amet, consectetur adipiscings do eiusmod tempor incididunt ut labore</p>
    <div class="card-btn">READ MORE <svg width="14" height="14" viewBox="0 0 14 14"><circle cx="7" cy="7" r="7" fill="var(--teal)"/><path d="M4 7h6M7 4l3 3-3 3" stroke="#fff" stroke-width="1.8" fill="none"/></svg></div>
    <div class="card-stats"><span><svg width="14" height="13" viewBox="0 0 14 13"><path d="M0 5h3v8H0zM4 5l3-5c1 0 2 1 1 3h5a1 1 0 010 3l-2 7H4z" fill="var(--red)"/></svg>300</span><span class="sep">|</span><span><svg width="16" height="13" viewBox="0 0 16 13" fill="none" stroke="var(--red)" stroke-width="1.6"><ellipse cx="8" cy="6" rx="7" ry="5"/></svg>150</span><span class="share"><svg width="14" height="13" viewBox="0 0 14 13" fill="var(--red)"><circle cx="11" cy="2.5" r="2.5"/><circle cx="3" cy="6.5" r="2.5"/><circle cx="11" cy="10.5" r="2.5"/><path d="M3 6.5L11 2.5M3 6.5l8 4" stroke="var(--red)" stroke-width="1.5"/></svg>15</span></div>
  </article>

  <article class="card" style="left:453px">
    <div class="card-photo photo-b" role="img" aria-label="Photo of a smiling winner in front of a stone fountain"></div>
    <svg class="card-curve" width="294" height="20" viewBox="0 0 294 20"><path d="M14 6 Q147 30 280 6 Q147 18 14 6Z" fill="var(--red)"/></svg>
    <h3 class="card-title">APRIL'S WINNER<br>PRIZE</h3>
    <p class="card-text">Lorem ipsum dolor sit amet, consectetur adipiscings do eiusmod tempor incididunt ut labore</p>
    <div class="card-btn card-btn--solid">READ MORE <svg width="14" height="14" viewBox="0 0 14 14"><circle cx="7" cy="7" r="7" fill="#fff"/><path d="M4 7h6M7 4l3 3-3 3" stroke="var(--teal)" stroke-width="1.8" fill="none"/></svg></div>
    <div class="card-stats"><span><svg width="14" height="13" viewBox="0 0 14 13"><path d="M0 5h3v8H0zM4 5l3-5c1 0 2 1 1 3h5a1 1 0 010 3l-2 7H4z" fill="var(--red)"/></svg>300</span><span class="sep">|</span><span><svg width="16" height="13" viewBox="0 0 16 13" fill="none" stroke="var(--red)" stroke-width="1.6"><ellipse cx="8" cy="6" rx="7" ry="5"/></svg>150</span><span class="share"><svg width="14" height="13" viewBox="0 0 14 13" fill="var(--red)"><circle cx="11" cy="2.5" r="2.5"/><circle cx="3" cy="6.5" r="2.5"/><circle cx="11" cy="10.5" r="2.5"/><path d="M3 6.5L11 2.5M3 6.5l8 4" stroke="var(--red)" stroke-width="1.5"/></svg>15</span></div>
  </article>

  <article class="card" style="left:794px">
    <div class="card-photo photo-c" role="img" aria-label="Photo of a smiling winner on a busy city square"></div>
    <svg class="card-curve" width="294" height="20" viewBox="0 0 294 20"><path d="M14 6 Q147 30 280 6 Q147 18 14 6Z" fill="var(--red)"/></svg>
    <h3 class="card-title">APRIL'S WINNER<br>PRIZE</h3>
    <p class="card-text">Lorem ipsum dolor sit amet, consectetur adipiscings do eiusmod tempor incididunt ut labore</p>
    <div class="card-btn">READ MORE <svg width="14" height="14" viewBox="0 0 14 14"><circle cx="7" cy="7" r="7" fill="var(--teal)"/><path d="M4 7h6M7 4l3 3-3 3" stroke="#fff" stroke-width="1.8" fill="none"/></svg></div>
    <div class="card-stats"><span><svg width="14" height="13" viewBox="0 0 14 13"><path d="M0 5h3v8H0zM4 5l3-5c1 0 2 1 1 3h5a1 1 0 010 3l-2 7H4z" fill="var(--red)"/></svg>300</span><span class="sep">|</span><span><svg width="16" height="13" viewBox="0 0 16 13" fill="none" stroke="var(--red)" stroke-width="1.6"><ellipse cx="8" cy="6" rx="7" ry="5"/></svg>150</span><span class="share"><svg width="14" height="13" viewBox="0 0 14 13" fill="var(--red)"><circle cx="11" cy="2.5" r="2.5"/><circle cx="3" cy="6.5" r="2.5"/><circle cx="11" cy="10.5" r="2.5"/><path d="M3 6.5L11 2.5M3 6.5l8 4" stroke="var(--red)" stroke-width="1.5"/></svg>15</span></div>
  </article>

  <footer class="footer">
    <div class="footer-col contact">
      <h4>Contact Us</h4>
      <p><svg width="16" height="16" viewBox="0 0 16 16"><path d="M3 1l3 3-2 2c1 2 3 4 6 6l2-2 3 3-2 2C7 15 1 9 1 3z" fill="#fff"/></svg>(+1)&nbsp; 555 014 2288</p>
      <p><svg width="16" height="12" viewBox="0 0 16 12"><rect width="16" height="12" rx="1" fill="#fff"/><path d="M0 1l8 6 8-6" stroke="var(--teal)" stroke-width="1.5" fill="none"/></svg>hello@wishcatcherclub.com</p>
    </div>
    <div class="footer-col follow">
      <h4>Follow Us On:</h4>
      <div class="socials">
        <span class="social"></span>
        <span class="social"><svg width="20" height="15" viewBox="0 0 16 12"><rect width="16" height="12" rx="1" fill="#fff"/><path d="M0 1l8 6 8-6" stroke="var(--teal)" stroke-width="1.5" fill="none"/></svg></span>
        <span class="social"></span>
      </div>
    </div>
    <div class="footer-rule"></div>
    <p class="copyright">Copyright © 2019 Wishcatcher. All Rights Reserved.</p>
    <div class="live">LIVE CART <svg width="20" height="16" viewBox="0 0 20 16" fill="none" stroke="#fff" stroke-width="1.8"><ellipse cx="8" cy="6" rx="7" ry="5"/><path d="M13 11c3 0 6-1 6-4"/></svg></div>
  </footer>

  <div class="brand brand--footer"><span class="brand-dot"></span>WISHCATCHER</div>
</div>
</body>
</html>
```